Book cover design front to back

Name of book: The Brannigan Hearth: An Irish Culinary Memoir
authoress: Maureen Brannigan
Front should be someone eating a white bread crisp sandwich (samples attached but cannot use as copyright)

Picture of me at the back as a kid the one with the hands on her face it should only be this one person. ideas welcome..
The text for back cover An Irish Culinary Memoir
Step inside the beautiful, noisy sanctuary of the Brannigan family kitchen—a place where the fire was always roaring, the tea was always brewing, and love was measured in hearty, home-cooked meals.

In this nostalgic and deeply personal memoir, the author takes you on a journey back to an Irish childhood filled with laughter, chaos, and the unforgettable characters who shaped it. At the center of it all are two free spirits: Mam, the undisputed ruler of the kitchen who commanded the stove with an iron fist and a heart of gold; and Dad, the resident fisherman and eccentric performer who kept everyone entertained (even when bringing home wild eels for dinner).

From hectic midweek lifesavers to the sacred rituals of the Saturday grocery convoy, The Brannigan Hearth is more than just a collection of family recipes. It is a joyful celebration of a happy childhood, a profound thank you to two remarkable parents, and a testament to the comforting food that sustained them all.

Pull up a chair, grab a cup of tea, and join the family. There’s always room at The Brannigan Hearth.

```html
<!DOCTYPE html>
<html lang="en">
<head>
<meta charset="utf-8">
<title>The Brannigan Hearth — Cover Spread</title>
<link rel="stylesheet" href="https://fonts.googleapis.com/css2?family=Pinyon+Script&family=Playfair+Display:wght@700;800&family=Cinzel:wght@500&family=Oswald:wght@500&family=Tinos&display=swap">
<style>
  :root{
    --bg:#e9e9ea;
    --green:#2f4a2c;
    --green-dark:#243a22;
    --cream:#f1e6c8;
    --parchment:#efe3c0;
    --parchment-edge:#d8c596;
    --ink:#2a2a22;
    --heading:#2f4a2c;
    --gold:#b88a4a;
    --sage:#a9c48a;
  }
  *{box-sizing:border-box;margin:0;padding:0}
  html,body{width:865px;height:1200px;overflow:hidden;background:var(--bg)}
  .spread{position:absolute;left:20px;top:345px;width:825px;height:509px;display:flex;box-shadow:0 6px 18px rgba(0,0,0,.25)}
  /* back cover */
  .back{position:relative;width:394px;height:100%;overflow:hidden;
    background:radial-gradient(ellipse at 70% 40%,#f6ecd0 0%,var(--parchment) 55%,var(--parchment-edge) 100%)}
  .back-photo{position:absolute;left:0;top:0;width:230px;height:100%;
    background:linear-gradient(180deg,#cfe0d8 0%,#c9a77e 22%,#b98360 45%,#a47b58 62%,#6f7a45 82%,#5d6c3a 100%);
    -webkit-mask-image:linear-gradient(90deg,#000 60%,transparent 100%);
    mask-image:linear-gradient(90deg,#000 60%,transparent 100%)}
  .back-copy{position:absolute;left:188px;top:46px;width:188px;font-family:"Tinos",serif;color:var(--ink)}
  .back-heading{font-family:"Oswald",sans-serif;font-weight:500;font-size:16.5px;color:var(--heading);text-align:right;letter-spacing:-.2px}
  .rule{display:flex;align-items:center;justify-content:center;gap:4px;margin:6px 0 7px 40px}
  .rule span{display:block;height:1px;width:44px;background:var(--gold)}
  .rule i{display:block;width:5px;height:5px;background:var(--gold);transform:rotate(45deg)}
  .back-copy p{font-size:8.6px;line-height:12.2px;text-align:justify;text-align-last:center;margin-bottom:6px}
  .back-copy p.invite{font-size:11.6px;line-height:15px;text-align:center;margin-top:12px;padding-left:4px}
  /* spine */
  .spine{position:relative;width:36px;height:100%;background:var(--green);border-left:1px solid var(--green-dark);border-right:1px solid var(--green-dark)}
  .spine-title{position:absolute;left:50%;top:50px;transform:translateX(-50%);writing-mode:vertical-rl;
    font-family:"Oswald",sans-serif;font-weight:500;font-size:15px;color:var(--cream)}
  .spine-author{position:absolute;left:50%;top:285px;transform:translateX(-50%);writing-mode:vertical-rl;
    font-family:"Cinzel",serif;font-size:8.5px;letter-spacing:2.5px;color:var(--cream)}
  .spine-rule{position:absolute;left:50%;width:1px;height:22px;background:var(--gold);transform:translateX(-50%)}
  .spine-dot{position:absolute;left:50%;width:5px;height:5px;border-radius:50%;border:1px solid var(--gold);transform:translateX(-50%)}
  /* front cover */
  .front{position:relative;width:395px;height:100%;overflow:hidden;
    background:radial-gradient(ellipse at 78% 30%,#c08a6a 0%,#7a4a2c 30%,transparent 55%),
               radial-gradient(ellipse at 45% 78%,#e7d6a6 0%,#b99a5e 18%,transparent 40%),
               linear-gradient(160deg,#6b5a36 0%,#4a3a22 40%,#3a2818 75%,#2c1d12 100%)}
  .title-block{position:absolute;left:10px;top:30px;width:210px;text-align:center;color:var(--cream)}
  .title-rule{display:flex;align-items:center;justify-content:center;gap:5px}
  .title-rule span{display:block;height:1px;width:38px;background:var(--sage)}
  .title-rule i{display:block;width:4px;height:4px;border-radius:50%;background:var(--sage)}
  .title-the{font-family:"Pinyon Script",cursive;font-size:40px;line-height:38px;margin-top:-14px}
  .title-main{font-family:"Playfair Display",serif;font-weight:800;font-size:40px;line-height:40px;letter-spacing:-.5px}
  .title-block .title-rule.lower{margin-top:8px}
  .subtitle{font-family:"Pinyon Script",cursive;font-size:20px;line-height:22px;color:var(--sage);margin-top:6px}
  .author-band{position:absolute;left:58px;right:0;top:463px;height:22px;
    background:linear-gradient(90deg,rgba(47,74,44,.4) 0%,var(--green) 20%,var(--green) 100%);
    font-family:"Cinzel",serif;font-size:12.5px;letter-spacing:3px;color:var(--cream);
    display:flex;align-items:center;justify-content:center}
</style>
</head>
<body>
  <main class="spread">
    <section class="back">
      <div class="back-photo" role="img" aria-label="Photograph of the author as a smiling freckled child resting her face in her hands, lying in clover"></div>
      <div class="back-copy">
        <h2 class="back-heading">An Irish Culinary Memoir</h2>
        <div class="rule"><span></span><i></i><span></span></div>
        <p>Step inside the beautiful, noisy sanctuary of the Brannigan family kitchen—a place where the fire was always roaring, the tea was always brewing, and love was measured in hearty, home-cooked meals.</p>
        <p>In this nostalgic and deeply personal memoir, the author takes you on a journey back to an Irish childhood filled with laughter, chaos, and the unforgettable characters who shaped it. At the center of it all are two free spirits: Mam, the undisputed ruler of the kitchen who commanded the stove with an iron fist and a heart of gold; and Dad, the resident fisherman and eccentric performer who kept everyone entertained (even when bringing home wild eels for dinner).</p>
        <p>From hectic midweek lifesavers to the sacred rituals of the Saturday grocery convoy, The Brannigan Hearth is more than just a collection of family recipes. It is a joyful celebration of a happy childhood, a profound thank you to two remarkable parents, and a testament to the comforting food that sustained them all.</p>
        <p class="invite">Pull up a chair, grab a cup of tea, and join the family. There’s always room at The Brannigan Hearth.</p>
      </div>
    </section>

    <section class="spine">
      <span class="spine-dot" style="top:14px"></span>
      <span class="spine-rule" style="top:22px"></span>
      <span class="spine-title">The Brannigan Hearth</span>
      <span class="spine-rule" style="top:252px"></span>
      <span class="spine-author">MAUREEN BRANNIGAN</span>
      <span class="spine-rule" style="top:465px"></span>
      <span class="spine-dot" style="top:490px"></span>
    </section>

    <section class="front" role="img" aria-label="Photograph of a curly-haired woman in a striped top eating a white bread crisp sandwich, with a second sandwich on a plate and a floral tea mug on a wooden table">
      <div class="title-block">
        <div class="title-rule"><span></span><i></i><span style="width:90px;opacity:0"></span><i></i><span></span></div>
        <div class="title-the">The</div>
        <div class="title-main">Brannigan</div>
        <div class="title-main">Hearth</div>
        <div class="title-rule lower"><span></span><i></i><span></span><i></i><span></span></div>
        <div class="subtitle">An Irish<br>Culinary Memoir</div>
      </div>
      <div class="author-band">MAUREEN BRANNIGAN</div>
    </section>
  </main>
</body>
</html>
```